Verpackungen für ein Deo
Zielgruppe
ZONK BR... ähm MAU! Wir benötigen ein Design für die Verpackung unseres Case. Statt einer typischen Schachtel, wollen wir ein Label um unser Case herumwickeln, das einerseits unser Case schützt, andererseits auf unser REFILL System aufmerksam macht und im Inneren auch erklärt, wie das Produkt funktioniert und unsere Story erzählt. Wir wollen unnötige Verpackung vermeiden - also am besten besteht das Label/die Verpackung aus einem Stück. Auch soll die Farbe des Cases gut sichtbar sein. Wir haben bereits ein grobes Schnittmuster angehängt, wie so ein Label aussehen könnte. Man muss sich aber nicht daran halten. Gerne eigene Ideen einfließen lassen. Unser Case ist ca. 8,3cm hoch und hat einen Durchmesser von ca. 4,6cm
Es handelt sich dabei um ein Refill Deo. Nähere Infos findet ihr auf unserer Homepage. https://www.zonk-mau.example/pages/refill-deo
Unsere Marke tritt jung, modern und auffällig auf.
Wir sind zwar nachhaltig, aber keineswegs langweilig.
Unsere Cases gibt es in sportlichen Farben. Wir wollen Menschen dabei unterstützen selbstsicher zu sein und lieben 'dad-jokes' Du darfst also auch laut sein.
Also tobe dich aus! Wir sind auf deine Ideen gespannt!
Aufgabenstellung
1.Müssen Sie nur die Vorderseite des Etiketts?
-> Das Etikett soll von Außen und Innen designed werden. Außen soll ganz klar sichtbar sein, dass es sich um ein Case für unser Refill Deo handelt. Innen wollen wir zeigen wie es funktioniert und kurz auf unsere Story aufmerksam machen. Siehe Anhang (Was muss drauf sein)
2. Wie groß ist das Fenster, das für den Druck der Chargennummer belassen werden soll? Und gibt es eine vorgeschriebene Stelle auf dem Etikett, an der sie angebracht werden muss?
-> Da das Case ohne Refill verkauft wird benötigen wir keine Chargennummer.
3. In der Aufgabe, die auf dem Etikett platziert werden muss, ist kein QR und EAN-Code enthalten. Soll ich nur die Code-Visualisierung einfügen oder wird der Code später zur Verfügung gestellt?
-> Genau. Code wird später zur Verfügung gestellt, bzw. bekommt jede Case Farbe einen eigenen Ean Code. Muss Mindestens 3x1,5cm groß sein
4.Es gibt kein NON GMO-Zeichen in der Aufgabe, das auf dem Etikett platziert werden muss. Soll ich nur die Code-Visualisierung platzieren oder wird das Schild später bereitgestellt?
-> wird nicht benötigt
5. Die Aufgabe enthält keine Zutaten- und Nährwerttabelle. Könntest du sie zum Wettbewerb hinzufügen?
-> Nicht benötigt. Das ist die Verpackung nur für das Case. Das Deo Refill wird seperat angeboten
6.Auf dem Etikett sollte Made in Germany(Österreich) stehen?
7. Welche Farbe und welche Schriftart möchten Sie verwenden? Dies ist für einen Designer sehr wichtig zu wissen.
-> Da unsere Cases sehr bunt sind, kann das Etikett schlicht gestaltet sein. Unsere CI Schriftart ist ROBOTO
-> CI Farben:
LIME / Neon Gelb
PANTONE 388 C
FARBWERTE:
RGB 224 231 34
HEX/HTML E0E722
CMYK 11 0 91 0
PINK / Neon Pin..

```html
<!DOCTYPE html>
<html lang="de">
<head>
<meta charset="utf-8">
<title>ZONK MAU! Refill Deo – Case-Etiketten</title>
<link rel="stylesheet" href="https://fonts.googleapis.com/css2?family=Roboto:wght@400;700;900&display=swap">
<style>
  :root {
    --page: #f1f1f1;
    --label-light: #e6e6e6;
    --label-dark: #151515;
    --pink: #e6258f;
    --ink: #151515;
    --white: #ffffff;
    --grey-text: #555555;
  }
  * { box-sizing: border-box; margin: 0; padding: 0; }
  html, body {
    width: 711px; height: 1200px; overflow: hidden;
    background: var(--page);
    font-family: "Roboto", Arial, sans-serif;
  }
  .sheet {
    width: 711px; height: 1200px;
    display: flex; flex-direction: column;
    justify-content: space-around; align-items: center;
    padding: 30px 0;
  }
  .label {
    width: 560px; height: 300px;
    display: flex;
    border-radius: 4px;
    overflow: hidden;
    box-shadow: 0 2px 6px rgba(0,0,0,0.08);
  }
  .label__info {
    width: 150px; padding: 26px 16px;
    font-size: 9px; line-height: 1.5;
  }
  .label__info h3 { font-size: 10px; font-weight: 700; margin-bottom: 8px; letter-spacing: 0.5px; }
  .label__info p { margin-bottom: 6px; }
  .label__band {
    width: 58px;
    display: flex; align-items: center; justify-content: center;
  }
  .label__band span {
    transform: rotate(-90deg);
    white-space: nowrap;
    font-weight: 900; font-size: 26px; letter-spacing: 1px;
  }
  .label__brand {
    flex: 1;
    display: flex; flex-direction: column; justify-content: center;
    padding-left: 48px;
    font-weight: 900; font-size: 96px; line-height: 0.92;
  }

  /* Variante Pink */
  .label--pink { background: var(--label-light); }
  .label--pink .label__info { color: var(--grey-text); }
  .label--pink .label__band { background: var(--pink); color: var(--white); }
  .label--pink .label__brand { color: var(--pink); }

  /* Variante Schwarz auf Hell */
  .label--mono { background: var(--label-light); }
  .label--mono .label__info { color: var(--grey-text); }
  .label--mono .label__band { background: var(--ink); color: var(--white); }
  .label--mono .label__brand { color: var(--ink); }

  /* Variante Weiß auf Schwarz */
  .label--dark { background: var(--label-dark); }
  .label--dark .label__info { color: #bdbdbd; }
  .label--dark .label__band { background: var(--label-light); color: var(--ink); }
  .label--dark .label__brand { color: var(--white); }
</style>
</head>
<body>
<main class="sheet">
  <section class="label label--pink">
    <div class="label__info">
      <h3>FLIP CASE</h3>
      <p>Einmal kaufen, immer nachfüllen.</p>
      <p>Refill rein, Deckel zu.</p>
      <p>Weniger Müll, mehr Mut.</p>
    </div>
    <div class="label__band"><span>REFILL DEO</span></div>
    <div class="label__brand"><span>ZONK</span><span>MAU!</span></div>
  </section>

  <section class="label label--mono">
    <div class="label__info">
      <h3>FLIP CASE</h3>
      <p>Einmal kaufen, immer nachfüllen.</p>
      <p>Refill rein, Deckel zu.</p>
      <p>Weniger Müll, mehr Mut.</p>
    </div>
    <div class="label__band"><span>REFILL DEO</span></div>
    <div class="label__brand"><span>ZONK</span><span>MAU!</span></div>
  </section>

  <section class="label label--dark">
    <div class="label__info">
      <h3>FLIP CASE</h3>
      <p>Einmal kaufen, immer nachfüllen.</p>
      <p>Refill rein, Deckel zu.</p>
      <p>Weniger Müll, mehr Mut.</p>
    </div>
    <div class="label__band"><span>REFILL DEO</span></div>
    <div class="label__brand"><span>ZONK</span><span>MAU!</span></div>
  </section>
</main>
</body>
</html>
```